Technology management company looking for a new website with a professional look

Brennick IT is a recently re-branded technology management company that is looking for a website design to match its personalized approach and friendly culture.

We would like to see a specialized, but related, page style for each of our main service offerings of:

• Commercial IT Support (This is our primary focus)
• Commercial Phone Systems (We partner with http://www.voxtrell.com/ for our phone systems)
• Point of Sale Systems (We partner with http://www.tillmora.com/ for our POS systems.
• Web Design
• Hollow Pine Computers (Our residential computer service offering, branded as Hollow Pine Computers)

The Hollow Pine Computers page should be build upon the Hollow Pine Computers logo, the other four pages should be branded as Brennick IT.

These five separate pages should have subtle, yet clearly defined links to one another. They should also each have a Home, Products, Service, and Company in the menu.

The website should have a clean design with professional appeal, but not appear too sterile or uninviting. It needs to have a simple, easy to navigate menu interface along the top. We would also like the site to be mobile friendly.

It should also allow us to easily tie in links to our social media pages (Facebook, LinkedIn, Twitter and Google+) and provide easy access to our contact information from each page.

This is a link to our old website www.hollowpinecomputers.com

We don't currently have copy available. The text and menu design should be easily editable and expandable so we can use the design to fit our copy.

In general we are looking for a concept we can modify to fit our needs.

We need this design to be available with layers in a .psd format.

Target Market(s)

Small to mid-size businesses.

Industry/Entity Type

Information Technology

Number of Pages Required

5+ page

Font styles to use
Sans Serif

Requirements
Must have
• Mobile Friendly
• Professional Type Face
• Unity between all pages
• .PSD Format
Nice to have
• Themed with our logo
Should not have
• Bubbly unprofessional typeface. No comic sans.

```html
<!DOCTYPE html>
<html lang="en">
<head>
<meta charset="utf-8">
<title>Brennick IT</title>
<link href="https://fonts.googleapis.com/css2?family=Open+Sans:wght@400;600;700&display=swap" rel="stylesheet">
<style>
:root{
  --navy:#0e2238;
  --navy-deep:#0a1a2c;
  --orange:#e2622a;
  --orange-band:#c9642f;
  --orange-dark:#a9501f;
  --blue:#2a7fc4;
  --ink:#33475b;
  --grey:#8a96a3;
  --footer:#2b2672;
  --footer-bar:#f4f4f6;
  --white:#ffffff;
}
*{box-sizing:border-box;margin:0;padding:0}
html,body{width:1200px;height:3224px;overflow:hidden}
body{position:relative;font-family:"Open Sans",Arial,sans-serif;color:var(--ink);background:var(--white)}
.abs{position:absolute}

/* header */
.site-header{left:0;top:0;width:1200px;height:80px;background:var(--white)}
.brand{left:120px;top:14px;display:flex;align-items:center;gap:12px}
.brand-dot{width:44px;height:44px;border-radius:50%;background:var(--orange);flex:none}
.brand-name{font-size:38px;font-weight:700;color:var(--navy);line-height:1;white-space:nowrap}
.contact-phone{right:120px;top:10px;font-size:11px;font-weight:600;color:var(--navy);letter-spacing:.3px}
.main-nav{right:116px;top:36px;display:flex;gap:26px;font-size:13px;font-weight:700;color:var(--navy)}

/* hero */
.hero{left:0;top:80px;width:1200px;height:430px;
  background:radial-gradient(circle at 70% 35%,#3f6f93 0%,#1b3b58 35%,#0e2238 70%);
  clip-path:polygon(0 0,100% 0,100% 78%,60% 100%,0 100%)}
.hero-glow{left:620px;top:100px;width:420px;height:380px;border-radius:50%;
  background:radial-gradient(circle,#c9d6e2 0%,rgba(201,214,226,.35) 40%,rgba(14,34,56,0) 70%)}
.hero-text{left:108px;top:222px;width:520px;color:var(--white)}
.hero-kicker{font-size:18px;font-weight:400}
.hero-title{font-size:46px;font-weight:400;line-height:1.15;margin-top:4px}
.hero-title b{font-weight:700}
.hero-lede{font-size:16px;line-height:1.3;margin-top:6px;color:#d8e2ec}
.btn{display:inline-block;background:var(--orange);color:var(--white);font-size:15px;font-weight:600;padding:10px 24px;border-radius:2px}
.hero-text .btn{margin-top:20px}

/* who we are */
.about-mark{left:130px;top:570px;display:flex;align-items:center;gap:16px}
.about-mark .brand-dot{width:120px;height:120px}
.about-mark .brand-name{font-size:30px}
.section-title{font-size:34px;font-weight:400;color:var(--navy)}
.about{left:600px;top:560px;width:540px}
.about p{font-size:14px;line-height:1.45;color:var(--grey);margin-top:14px}
.about .btn{margin-top:22px}

/* services */
.services-title{left:0;top:880px;width:1200px;text-align:center}
.service{top:945px;width:220px;text-align:center}
.service-icon{width:76px;height:76px;margin:0 auto;display:block}
.service h3{font-size:15px;font-weight:700;color:var(--navy);margin-top:14px;line-height:1.25;min-height:38px}
.service p{font-size:12px;color:var(--grey);line-height:1.4;margin-top:6px}

/* clients */
.clients-band{left:0;top:1195px;width:1200px;height:600px}
.clients-title{left:0;top:1290px;width:1200px;text-align:center;color:var(--white);font-size:44px;font-weight:400}
.client-name{left:190px;top:1470px;color:var(--white)}
.client-name h3{font-size:36px;font-weight:600}
.client-name p{font-size:16px;margin-top:2px}
.client-photo{left:470px;top:1415px;width:210px;height:210px;border-radius:50%;border:6px solid #f0e3da;
  background:linear-gradient(160deg,#7aa0c4,#5a7894 60%,#3e5568)}
.client-quote{left:720px;top:1450px;width:400px;color:var(--white);font-size:16px;line-height:1.4}
.dots{display:flex;gap:9px}
.dot{width:10px;height:10px;border-radius:50%;background:rgba(255,255,255,.55)}
.dot.on{background:var(--white)}
.client-dots{left:572px;top:1706px}

/* featured */
.featured-title{left:0;top:1822px;width:1200px;text-align:center;color:var(--blue);font-size:48px}
.feature{top:1915px;width:300px;text-align:center}
.hex{margin:0 auto;clip-path:polygon(25% 4%,75% 4%,100% 50%,75% 96%,25% 96%,0 50%)}
.feature .hex{width:250px;height:230px}
.feature h3{font-size:16px;font-weight:600;color:var(--navy);margin-top:18px}
.feature p{font-size:13px;color:var(--grey);line-height:1.4;margin-top:6px;padding:0 40px}

/* blogs */
.blogs-band{left:0;top:2280px;width:1200px;height:610px}
.blogs-title{left:0;top:2372px;width:1200px;text-align:center;color:var(--white);font-size:48px}
.post{top:2470px;width:300px;text-align:center;color:var(--white)}
.post .hex{width:190px;height:175px}
.post h3{font-size:16px;font-weight:400;margin-top:20px}
.post time{display:block;font-size:14px;margin-top:2px}
.post p{font-size:14px;line-height:1.4;margin-top:4px;padding:0 35px}
.blog-dots{left:580px;top:2845px}

/* footer */
.site-footer{left:0;top:2880px;width:1200px;height:300px;background:var(--footer);color:var(--white)}
.footer-col{color:var(--white)}
.footer-col h4{font-size:22px;font-weight:400;margin-bottom:10px}
.links{left:118px;top:2955px}
.links li{list-style:none;font-size:15px;line-height:1.5}
.contact{left:420px;top:2955px}
.contact-row{display:flex;align-items:center;gap:14px;margin-top:18px;font-size:15px;line-height:1.3}
.contact-phone-big{font-size:20px}
.address{left:780px;top:2960px;display:flex;gap:16px;font-size:14px;line-height:1.4;color:var(--white)}
.footer-bar{left:0;top:3180px;width:1200px;height:44px;background:var(--footer-bar);text-align:center;font-size:13px;line-height:44px;color:var(--ink)}
</style>
</head>
<body>

<header class="site-header abs">
  <div class="brand abs"><span class="brand-dot"></span><span class="brand-name">Brennick IT</span></div>
  <div class="contact-phone abs">CONTACT PHONE: 1 555 010 4477</div>
  <nav class="main-nav abs"><span>HOME</span><span>ABOUT</span><span>TEAM</span><span>SERVICES</span><span>APPROACH</span><span>CONTACT US</span></nav>
</header>

<section class="hero abs" role="img" aria-label="Photo of a businesswoman touching a glowing digital network display"></section>
<div class="hero-glow abs"></div>
<div class="hero-text abs">
  <p class="hero-kicker">Brennick IT helps clients gain confidence</p>
  <h1 class="hero-title"><b>Process</b> Excellence</h1>
  <p class="hero-lede">Sed ut perspiciatis unde omnis iste natus error sit voluptatem accusantium doloremque</p>
  <span class="btn">Discover More</span>
</div>

<div class="about-mark abs"><span class="brand-dot"></span><span class="brand-name">Brennick IT</span></div>
<section class="about abs">
  <h2 class="section-title">Who We Are</h2>
  <p>Buyers want vendors to help them but few they'll be founded by sales or spammed by emailing so they reject web forms and remain anonymous.</p>
  <p>Our Protected Buyer Engagement Platform enables vendors to connect and help anonymous visitors get the answers they need.</p>
  <span class="btn">Discover More</span>
</section>

<h2 class="section-title services-title abs">Our Services</h2>
<div class="service abs" style="left:130px">
  <svg class="service-icon" viewBox="0 0 76 76"><circle cx="38" cy="38" r="34" fill="none" stroke="#e2622a" stroke-width="6"/><circle cx="38" cy="38" r="22" fill="#2a7fc4"/></svg>
  <h3>Financial and Insurance Industry Experts</h3>
  <p>Buyers want vendors to help them but fear they'll be hounded by sales or spammed by emailing.</p>
</div>
<div class="service abs" style="left:370px">
  <svg class="service-icon" viewBox="0 0 76 76"><circle cx="38" cy="38" r="34" fill="none" stroke="#e2622a" stroke-width="6"/><circle cx="38" cy="38" r="22" fill="#2a7fc4"/></svg>
  <h3>Customer Service</h3>
  <p>Buyers want vendors to help them but fear they'll be hounded by sales or spammed by emailing.</p>
</div>
<div class="service abs" style="left:610px">
  <svg class="service-icon" viewBox="0 0 76 76"><circle cx="38" cy="38" r="34" fill="none" stroke="#e2622a" stroke-width="6"/><circle cx="38" cy="38" r="22" fill="#2a7fc4"/></svg>
  <h3>Regulatory</h3>
  <p>Buyers want vendors to help them but fear they'll be hounded by sales or spammed by emailing.</p>
</div>
<div class="service abs" style="left:850px">
  <svg class="service-icon" viewBox="0 0 76 76"><circle cx="38" cy="38" r="34" fill="none" stroke="#e2622a" stroke-width="6"/><circle cx="38" cy="38" r="22" fill="#2a7fc4"/></svg>
  <h3>Record Keeping and Accounting</h3>
  <p>Buyers want vendors to help them but fear they'll be hounded by sales or spammed by emailing.</p>
</div>

<svg class="clients-band abs" viewBox="0 0 1200 600" preserveAspectRatio="none">
  <polygon points="0,20 1200,0 1200,560 1120,600 0,600" fill="#c9642f"/>
  <polygon points="0,60 1200,60 1200,200 0,200" fill="#a9501f"/>
  <polygon points="0,600 0,520 80,600" fill="#ffffff"/>
  <polygon points="1200,600 1200,560 1120,600" fill="#ffffff"/>
</svg>
<h2 class="clients-title abs">Our Happy Clients</h2>
<div class="client-name abs"><h3>Mirela Castan</h3><p>Accountant Manager</p></div>
<div class="client-photo abs" role="img" aria-label="Portrait photo of a smiling client"></div>
<p class="client-quote abs">Lorem ipsum dolor sit amet, consectetur adipiscing elit, sed do eiusmod tempor incididunt ut labore et dolore magna aliqua. Ut enim ad minim veniam, quis nostrud exercitation.</p>
<div class="dots client-dots abs"><span class="dot on"></span><span class="dot"></span><span class="dot"></span></div>

<h2 class="section-title featured-title abs">Featured Services</h2>
<div class="feature abs" style="left:100px">
  <div class="hex" role="img" aria-label="Photo of business people in suits shaking hands" style="background:linear-gradient(160deg,#d7dde3,#6d7f92 60%,#2d3a48)"></div>
  <h3>Broker Dealer Service</h3>
  <p>A mutual fund company call center realized that 40% of the calls they took were calls.</p>
</div>
<div class="feature abs" style="left:450px">
  <div class="hex" role="img" aria-label="Photo of a glass office tower seen from below" style="background:linear-gradient(170deg,#9fc4d8,#4f7f8e 55%,#263f4a)"></div>
  <h3>Custodial And Trust</h3>
  <p>A mutual fund company call center realized that 40% of the calls they took were calls.</p>
</div>
<div class="feature abs" style="left:810px">
  <div class="hex" role="img" aria-label="Photo of a team meeting in an office" style="background:linear-gradient(160deg,#e6e3dc,#a09a8d 55%,#4a4a52)"></div>
  <h3>Wealth Management</h3>
  <p>A mutual fund company call center realized that 40% of the calls they took were calls.</p>
</div>

<svg class="blogs-band abs" viewBox="0 0 1200 610" preserveAspectRatio="none">
  <polygon points="0,40 60,0 1140,0 1200,40 1200,610 0,610" fill="#0a1a2c"/>
</svg>
<h2 class="section-title blogs-title abs">Our Blogs</h2>
<article class="post abs" style="left:100px">
  <div class="hex" role="img" aria-label="Photo of a handshake over a desk" style="background:linear-gradient(160deg,#e2ddd3,#96897a 55%,#3c3630)"></div>
  <h3>Darren Holloway</h3><time>6/11/2015 12:53 PM</time>
  <p>A mutual fund company call center realized that 40% of the calls they took were calls that the customer didn't want to make.</p>
</article>
<article class="post abs" style="left:450px">
  <div class="hex" role="img" aria-label="Photo of two people shaking hands" style="background:linear-gradient(160deg,#dfe6ec,#8899aa 55%,#34414f)"></div>
  <h3>Darren Holloway</h3><time>6/11/2015 12:53 PM</time>
  <p>A mutual fund company call center realized that 40% of the calls they took were calls that the customer didn't want to make.</p>
</article>
<article class="post abs" style="left:800px">
  <div class="hex" role="img" aria-label="Photo of a colleague presenting at a laptop" style="background:linear-gradient(160deg,#eeeae4,#a7a39b 55%,#4b4d55)"></div>
  <h3>Darren Holloway</h3><time>6/11/2015 12:53 PM</time>
  <p>A mutual fund company call center realized that 40% of the calls they took were calls that the customer didn't want to make.</p>
</article>
<div class="dots blog-dots abs"><span class="dot on"></span><span class="dot"></span><span class="dot"></span></div>

<footer class="site-footer abs"></footer>
<div class="footer-col links abs">
  <h4>Useful Links</h4>
  <ul><li>Home</li><li>Team</li><li>Service</li><li>Contact Us</li><li>About</li></ul>
</div>
<div class="footer-col contact abs">
  <h4>Contact details</h4>
  <div class="contact-row">
    <svg width="34" height="26" viewBox="0 0 34 26"><rect x="1" y="1" width="32" height="24" rx="2" fill="none" stroke="#fff" stroke-width="2"/><polyline points="2,3 17,15 32,3" fill="none" stroke="#fff" stroke-width="2"/></svg>
    <span>Email us<br>info@brennickit.com</span>
  </div>
  <div class="contact-row">
    <svg width="34" height="34" viewBox="0 0 24 24"><path fill="#fff" d="M6.6 10.8a15.1 15.1 0 0 0 6.6 6.6l2.2-2.2c.3-.3.7-.4 1-.2 1.1.4 2.3.6 3.6.6.6 0 1 .4 1 1V20c0 .6-.4 1-1 1A17 17 0 0 1 3 4c0-.6.4-1 1-1h3.5c.6 0 1 .4 1 1 0 1.3.2 2.5.6 3.6.1.3 0 .7-.2 1z"/></svg>
    <span>Call us on<br><span class="contact-phone-big">(555) 014-2288</span></span>
  </div>
</div>
<div class="address abs">
  <svg width="24" height="34" viewBox="0 0 24 34"><path fill="#fff" d="M12 0C5.4 0 0 5.2 0 11.7 0 20.5 12 34 12 34s12-13.5 12-22.3C24 5.2 18.6 0 12 0zm0 16.5a5 5 0 1 1 0-10 5 5 0 0 1 0 10z"/></svg>
  <span>4 Alder Court<br>Marrowfield Business Park<br>Tenley Road<br>Ashbury<br>Corvale<br>AB12 3CD</span>
</div>
<div class="footer-bar abs">© 2015 Brennick IT. All Rights Reserved</div>

</body>
</html>
```